WP website design Pine Harbor (Contest)

We need a wordpress design that will incorporate a professional color scheme with company logo in a clean layout. The design needs to consider that this will be developed on a responsive theme. Colors are blue and green of the logo and and an accent color (perhaps very light brown/tan). Client wants a 'modern' look.

Industry/Entity Type

It Company

Font styles to use
Serif
Sans Serif

Colors

Designer to choose colors to be used in the design.

Requirements
Must have
• Navigation: 1) Home; 2) Upcoming Auctions; 3) Past Auctions; 4) About Us; 5) Services; 6) Sellers; 7) Buyers; 8) Contact Us

Site will have slideshow - image is attached. Colors will be those in the logo, blue and green with maybe an accent color. A site the client mentions liking is trevalleauctions.com for the use of color and layout.

Widgets: 1) Featured Properties; 2) Call to action for Sellers 3) Testimonials blog/widget
Nice to have
• use of dropdown menus

```html
<!DOCTYPE html>
<html lang="en">
<head>
<meta charset="utf-8">
<title>Pine Harbor Auction &amp; Real Estate</title>
<link rel="stylesheet" href="https://fonts.googleapis.com/css2?family=Open+Sans:wght@400;600;700&family=Oswald:wght@500&family=Arimo:wght@400&family=Libre+Baskerville:ital@1&display=swap">
<style>
:root{
  --navy:#0f2d57;
  --navy-text:#1b3f74;
  --green:#13804f;
  --green-dark:#0b6a40;
  --green-light:#27a068;
  --ink:#1a1a1a;
  --body:#555;
  --muted:#777;
  --line:#e2e2e2;
  --band:#dcdcdc;
  --footer:#1b1b1b;
  --footer-base:#121212;
  --footer-text:#cfcfcf;
}
*{margin:0;padding:0;box-sizing:border-box}
html,body{width:1200px;height:2344px;overflow:hidden;background:#fff}
body{position:relative;font-family:"Arimo",Arial,sans-serif;color:var(--ink)}
.abs{position:absolute}

.topline{left:0;top:0;width:1200px;height:5px;background:var(--navy)}
.site-header{left:0;top:5px;width:1200px;height:107px;background:#fff}
.brand{left:144px;top:33px;display:flex;align-items:center;gap:12px}
.brand-mark{width:26px;height:26px;border-radius:50%;background:var(--green)}
.brand-name{font-family:"Open Sans",sans-serif;font-weight:700;font-size:17px;line-height:20px;color:var(--green-dark)}
.search{left:786px;top:39px;width:273px;height:34px;border:1px solid #d6d6d6;font-family:"Open Sans",sans-serif;font-size:12px;color:#999;padding:9px 22px}
.search svg{position:absolute;right:12px;top:8px}

.main-nav{left:0;top:112px;width:1200px;height:60px;background:linear-gradient(#20955f,#0c6c43);border-bottom:3px solid #e9efec}
.main-nav ul{list-style:none;display:flex;position:absolute;left:148px;top:18px}
.main-nav li{font-family:"Open Sans",sans-serif;font-weight:600;font-size:15px;color:#fff;margin-right:51px}
.main-nav li:last-child{margin-right:0}

.hero{left:0;top:172px;width:1200px;height:558px;background:linear-gradient(#6c8a5a 0%,#8a7768 10%,#9c846e 22%,#8d8a62 38%,#8cb7d6 44%,#6f99c2 54%,#76a23d 62%,#3f7f24 80%,#2f6a1c 100%)}
.hero-caption{left:139px;top:602px;width:922px;height:128px;background:rgba(18,50,96,.9)}
.hero-caption h1{position:absolute;left:46px;top:28px;font-family:"Open Sans",sans-serif;font-weight:700;font-size:28px;color:#fff;letter-spacing:.3px}
.hero-caption p{position:absolute;left:46px;top:70px;font-family:"Open Sans",sans-serif;font-weight:600;font-size:13.5px;color:#fff}
.dots{position:absolute;right:46px;top:68px;display:flex;gap:6px}
.dots span{width:12px;height:12px;border-radius:50%;border:1.5px solid #fff}
.dots span:first-child{background:#fff;box-shadow:inset 0 0 0 2px var(--navy)}

.section-title{font-family:"Oswald",sans-serif;font-weight:500;font-size:26px;color:var(--ink);letter-spacing:.2px}
.welcome-title{left:141px;top:772px}
.photo-frame{border:1px solid var(--line);padding:6px;background:#fff;box-shadow:0 1px 3px rgba(0,0,0,.08)}
.photo{width:100%;height:100%}
.welcome-photo{left:139px;top:836px;width:250px;height:176px}
.welcome-text{left:427px;top:830px;width:634px;font-size:11.6px;line-height:19.3px;color:var(--body);text-align:justify}
.btn-read{left:431px;top:970px;width:102px;height:41px;background:var(--green-dark);color:#fff;font-family:"Open Sans",sans-serif;font-size:13px;text-align:center;line-height:41px}

.featured-title{left:141px;top:1046px}
.arrows{left:1014px;top:1050px}

.card{width:203px}
.card .photo-frame{height:173px}
.card h3{margin-top:14px;font-family:"Open Sans",sans-serif;font-weight:600;font-size:15.5px;color:var(--navy-text)}
.card p{margin-top:7px;font-size:11.2px;line-height:19px;color:var(--muted)}
.card .price{margin-top:5px;font-size:13px;color:var(--ink)}
.card .price b{font-weight:400;color:var(--navy-text)}
.card hr{margin-top:13px;border:0;height:4px;background:#e6e6e6}

.testimonials{left:0;top:1791px;width:1200px;height:223px;background:linear-gradient(90deg,#cfcfcf,#e4e4e4 50%,#d4d4d4)}
.testimonials h2{position:absolute;left:146px;top:30px}
.avatar{position:absolute;left:148px;top:81px;width:102px;height:102px;border-radius:50%;border:4px solid #fff;background:radial-gradient(#e9c8a9,#b98a66)}
.quote{position:absolute;left:289px;top:94px;width:745px;font-size:11.2px;line-height:19.5px;color:#7a7a7a}
.qmark{position:absolute;font-family:"Libre Baskerville",serif;font-size:30px;color:#777;line-height:1}
.author{position:absolute;left:289px;top:170px;font-family:"Libre Baskerville",serif;font-style:italic;font-size:13px;color:#333}

.site-footer{left:0;top:2014px;width:1200px;height:250px;background:var(--footer)}
.footer-col{position:absolute;top:50px}
.footer-col h4{font-family:"Open Sans",sans-serif;font-weight:600;font-size:15px;color:#fff}
.quick-links{list-style:disc;margin-top:20px;padding-left:16px;color:#fff}
.quick-links li{font-family:"Open Sans",sans-serif;font-size:11.5px;line-height:18.7px;color:var(--footer-text)}
.signup{margin-top:22px;width:258px;height:36px;background:#101010;border:1px solid #2a2a2a;position:relative;font-family:"Open Sans",sans-serif;font-size:11.5px;color:#bbb;padding:10px 18px}
.signup span{position:absolute;right:6px;top:5px;width:82px;height:26px;background:var(--green);color:#fff;font-size:14px;text-align:center;line-height:26px}
.contact-list{margin-top:20px;font-family:"Open Sans",sans-serif;font-size:11.5px;color:var(--footer-text)}
.contact-list div{display:flex;align-items:center;gap:12px;height:25px}
.contact-list .indent{padding-left:25px}
.social{display:flex;gap:12px;margin-top:24px}
.social span{width:31px;height:31px;background:#4a4a4a}
.copyright{left:0;top:2264px;width:1200px;height:80px;background:var(--footer-base);font-family:"Open Sans",sans-serif;font-size:12px;color:#cfcfcf;text-align:center;line-height:72px}
</style>
</head>
<body>
<div class="abs topline"></div>
<header class="abs site-header">
  <div class="abs brand" style="top:28px"><span class="brand-mark"></span><span class="brand-name">Pine Harbor<br>Auction &amp; Real Estate</span></div>
  <div class="abs search" style="top:34px">Search here...
    <svg width="20" height="20" viewBox="0 0 20 20"><circle cx="8" cy="8" r="6" fill="none" stroke="#aaa" stroke-width="2"/><path d="M12.5 12.5l5 5" stroke="#aaa" stroke-width="2.5"/></svg>
  </div>
</header>
<nav class="abs main-nav">
  <ul><li>Home</li><li>Upcoming Auctions</li><li>Past Auctions</li><li>About Us</li><li>Services</li><li>Sellers</li><li>Buyers</li><li>Contact Us</li></ul>
</nav>

<section class="abs hero" role="img" aria-label="Slideshow photo of farm fields and crops beside a river"></section>
<div class="abs hero-caption">
  <h1>ALLIED ACRES REALTY</h1>
  <p>Lorem ipsum dolor sit amet, consectetuer adipiscing elit. Aenean commodo ligula eget dolor.</p>
  <div class="dots"><span></span><span></span><span></span><span></span></div>
</div>

<h2 class="abs section-title welcome-title">WELCOME TO OUR SITE !</h2>
<div class="abs photo-frame welcome-photo"><div class="photo" role="img" aria-label="Modern white house with pool at dusk" style="background:linear-gradient(#3d5fa8,#8aa2c8 55%,#6b5846 70%,#4f8db0)"></div></div>
<p class="abs welcome-text">Lorem ipsum dolor sit amet, consectetuer adipiscing elit. Aenean commodo ligula eget dolor. Aenean massa. Cum sociis natoque penatibus et magnis dis parturient montes, nascetur ridiculus mus. Donec quam felis, ultricies nec, pellentesque eu, pretium quis, sem. Nulla consequat massa quis enim. Donec pede justo, fringilla vel, aliquet nec, vulputate eget, arcu. In enim justo, rhoncus ut, imperdiet a, venenatis vitae, justo.Nullam dictum felis eu pede mollis pretium. Integer tincidunt.Cras dapibus. Vivamus elementum semper nisi. Aenean vulputate eleifend tellus. Aenean leo ligula, porttitor eu, consequat vitae, eleifend ac, enim. Aliquam lorem ante, dapibus</p>
<div class="abs btn-read">Read More</div>

<h2 class="abs section-title featured-title">FEATURED PROPERTIES</h2>
<svg class="abs arrows" width="46" height="30" viewBox="0 0 46 30"><path d="M16 4L6 15l10 11" fill="none" stroke="#ccc" stroke-width="2"/><path d="M30 4l10 11-10 11" fill="none" stroke="#ccc" stroke-width="2"/></svg>

<article class="abs card" style="left:139px;top:1105px"><div class="photo-frame"><div class="photo" role="img" aria-label="Modern villa with lit pool at night" style="background:linear-gradient(#17234f,#3a4f7a 40%,#8a7a5a 60%,#1e9fe0 80%,#4f5a6a)"></div></div><h3>Farm, Machinery</h3><p>Veltrano recognizes the middle east and greater asia</p><div class="price">Price: <b>HK$ 260,000,000</b></div><hr></article>
<article class="abs card" style="left:380px;top:1105px"><div class="photo-frame"><div class="photo" role="img" aria-label="White modern building with reflecting pool" style="background:linear-gradient(#5b8fc6,#b9cfe6 45%,#e9eef2 60%,#3f6f9a)"></div></div><h3>Equipment Properties</h3><p>veltrano recognizes the middle east and greater asia</p><div class="price">Price: <b>HK$ 260,000,000</b></div><hr></article>
<article class="abs card" style="left:614px;top:1105px"><div class="photo-frame"><div class="photo" role="img" aria-label="Dark modern house lit at night" style="background:linear-gradient(#1a3a7c,#20366a 45%,#d09a3a 65%,#1d2a1c)"></div></div><h3>Household &amp; Estate</h3><p>veltrano recognizes the middle east and greater asia</p><div class="price">Price: <b>HK$ 260,000,000</b></div><hr></article>
<article class="abs card" style="left:852px;top:1105px"><div class="photo-frame"><div class="photo" role="img" aria-label="Colourful town buildings along a street" style="background:linear-gradient(90deg,#d9b23a,#e8c96a 40%,#d24a3a 70%,#b83a30)"></div></div><h3>Field Cattle Properties</h3><p>veltrano recognizes the middle east and greater asia</p><div class="price">Price: <b>HK$ 260,000,000</b></div><hr></article>

<article class="abs card" style="left:139px;top:1441px"><div class="photo-frame"><div class="photo" role="img" aria-label="Wooden house with garage among trees" style="background:linear-gradient(#7f8fb8,#a9b4cc 35%,#6a4a36 65%,#4a5a3a)"></div></div><h3>Farm, Machinery</h3><p>Veltrano recognizes the middle east and greater asia</p><div class="price">Price: <b>HK$ 260,000,000</b></div><hr></article>
<article class="abs card" style="left:380px;top:1441px"><div class="photo-frame"><div class="photo" role="img" aria-label="Mediterranean villa with pool" style="background:linear-gradient(#4f86c4,#9cbde0 35%,#e2d3b0 60%,#22a6e0)"></div></div><h3>Equipment Properties</h3><p>veltrano recognizes the middle east and greater asia</p><div class="price">Price: <b>HK$ 260,000,000</b></div><hr></article>
<article class="abs card" style="left:614px;top:1441px"><div class="photo-frame"><div class="photo" role="img" aria-label="Classical white mansion with columns" style="background:linear-gradient(#e8edf2,#f3efe6 40%,#d9d2c2 70%,#3e5a2c)"></div></div><h3>Household &amp; Estate</h3><p>veltrano recognizes the middle east and greater asia</p><div class="price">Price: <b>HK$ 260,000,000</b></div><hr></article>
<article class="abs card" style="left:852px;top:1441px"><div class="photo-frame"><div class="photo" role="img" aria-label="Large stone estate with palm trees" style="background:linear-gradient(#6f92c8,#a8bedc 35%,#8a7a60 60%,#4a5a40)"></div></div><h3>Field Cattle Properties</h3><p>veltrano recognizes the middle east and greater asia</p><div class="price">Price: <b>HK$ 260,000,000</b></div><hr></article>

<section class="abs testimonials" aria-label="Testimonials">
  <h2 class="section-title">TESTIMONIALS</h2>
  <div class="avatar" role="img" aria-label="Portrait photo of the client"></div>
  <span class="qmark" style="left:260px;top:88px">&ldquo;</span>
  <p class="quote">Lorem ipsum dolor sit amet, consectetur adipisicing elit, sed do eiusmod tempor incididunt ut labore et dolore magna aliqua. Ut enim ad minim veniam, quis nostrud exercitation ullamco laboris nisi ut aliquip ex ea commodo consequat. Duis aute irure dolor in reprehenderit in voluptate velit esse cillum dolore eu fugiat nulla pariatur. consectetur commodo consequat. Duis aute irure dolor in reprehenderit in voluptate</p>
  <span class="qmark" style="left:867px;top:140px">&rdquo;</span>
  <div class="author">- JANETIE DOE</div>
</section>

<footer class="abs site-footer">
  <div class="footer-col" style="left:144px"><h4>QUICK LINKS</h4>
    <ul class="quick-links"><li>Home</li><li>Auctions</li><li>Real Estate Listings</li><li>Buyers</li><li>Sellers</li><li>About Us</li><li>Contact Us</li></ul></div>
  <div class="footer-col" style="left:328px"><h4>CALL TO ACTION FOR SELLERS</h4>
    <div class="signup">Enter your email here<span>Send</span></div></div>
  <div class="footer-col" style="left:634px"><h4>CONTACT</h4>
    <div class="contact-list">
      <div><svg width="16" height="14" viewBox="0 0 16 14"><path d="M1 5c0-3 14-3 14 0l-3 1-1-2H5L4 6zM4 7h8l2 6H2z" fill="#aaa"/></svg>Phone: (123) 1213 4656 789</div>
      <div><svg width="16" height="12" viewBox="0 0 16 12"><rect x="1" y="1" width="14" height="10" fill="none" stroke="#aaa" stroke-width="1.5"/><path d="M1 1l7 6 7-6" fill="none" stroke="#aaa" stroke-width="1.5"/></svg>Email: info@pineharborauctions.com</div>
      <div><svg width="16" height="18" viewBox="0 0 16 18"><path d="M8 1a6 6 0 0 0-6 6c0 4 6 10 6 10s6-6 6-10a6 6 0 0 0-6-6z" fill="#aaa"/><circle cx="8" cy="7" r="2.3" fill="#1b1b1b"/></svg>Address: Street Name ,City</div>
      <div class="indent">Street Name ,City</div>
    </div></div>
  <div class="footer-col" style="left:886px"><h4>FOLLOW US ON</h4>
    <div class="social"><span aria-label="Social link"></span><span aria-label="Social link"></span><span aria-label="Social link"></span><span aria-label="Feed link"></span></div></div>
</footer>
<div class="abs copyright">Copyright 2014pineharborauctions.com |&nbsp; All Rights Reserved.</div>
</body>
</html>
```